Marta Business Card

My wife is going to start her own business with renting holiday appartments to tourists. She needs a design for a new business card... and a new web site.
Look at Stayvolt "Erholung auf dem Lindenwäldchen"

Target Market(s)

Give business card to prospects at any situation

Contact Information for Business Card

not sure what this means

Font styles to use
Script

Colors
fec41a
fee18a

Requirements
Must have
• My wife's handwriting is difficult to read:
Entspannen - Loslassen - Auftanken
Marta & das Lindenwäldchen
Urlaub an einem besonderen Ort
Marta Brecke
Grauer Pfad 7
18471 Alt Feldow
post@marta-brecke.de
www.lindenwaeldchen.net
Nice to have
• Beige background
Font like handwriting

```html
<!DOCTYPE html>
<html lang="de">
<head>
<meta charset="utf-8">
<title>Marta Brecke – Visitenkarte</title>
<link rel="stylesheet" href="https://fonts.googleapis.com/css2?family=Alex+Brush&family=Questrial&display=swap">
<style>
  :root {
    --backdrop: #2b2b2d;
    --card: #221e1f;
    --gold: #fec41a;
    --gold-light: #fee18a;
    --gold-text: #f2d787;
    --rule: #d9a41c;
  }
  * { margin: 0; padding: 0; box-sizing: border-box; }
  html, body {
    width: 1200px;
    height: 900px;
    overflow: hidden;
    background: var(--backdrop);
  }
  .stage {
    width: 1200px;
    height: 900px;
    display: flex;
    align-items: center;
    justify-content: center;
  }
  .business-card {
    position: relative;
    width: 1050px;
    height: 600px;
    background: var(--card);
    border-radius: 48px;
    color: var(--gold-text);
    text-align: center;
  }
  .tagline {
    position: absolute;
    top: 62px;
    left: 0;
    right: 0;
    font-family: "Alex Brush", cursive;
    font-size: 68px;
    line-height: 78px;
    color: var(--gold-text);
  }
  .tagline span { display: block; }
  .divider {
    position: absolute;
    top: 352px;
    left: 80px;
    right: 80px;
    height: 2px;
    background: var(--rule);
  }
  .ornament {
    position: absolute;
    top: 326px;
    left: 50%;
    width: 150px;
    height: 54px;
    margin-left: -75px;
    border-radius: 50%;
    background: radial-gradient(ellipse at center, var(--gold) 0%, #c79315 55%, var(--card) 80%);
  }
  .contact {
    position: absolute;
    top: 402px;
    left: 0;
    right: 0;
    font-family: "Questrial", sans-serif;
    font-size: 30px;
    line-height: 50px;
    color: var(--gold-text);
  }
  .contact-line {
    display: flex;
    align-items: center;
    justify-content: center;
    gap: 12px;
  }
  .contact-line svg { width: 26px; height: 26px; }
  .address { margin-top: 22px; letter-spacing: 0.5px; }
</style>
</head>
<body>
  <main class="stage">
    <article class="business-card">
      <h1 class="tagline">
        <span>Entspannen - Loslassen - Auftanken</span>
        <span>Marta &amp; das Lindenwäldchen</span>
        <span>Urlaub an einem besonderen Ort</span>
      </h1>

      <div class="divider"></div>
      <div class="ornament" role="img" aria-label="Goldenes Zierornament in der Mitte der Trennlinie"></div>

      <address class="contact">
        <p class="contact-line">
          <svg viewBox="0 0 24 24" aria-hidden="true">
            <rect x="2" y="5" width="20" height="14" rx="2" fill="var(--gold)"/>
            <path d="M3 6 L12 13 L21 6" fill="none" stroke="var(--card)" stroke-width="1.6"/>
          </svg>
          post@marta-brecke.de
        </p>
        <p class="contact-line">
          <svg viewBox="0 0 24 24" aria-hidden="true">
            <circle cx="12" cy="12" r="10" fill="var(--gold)"/>
            <g fill="none" stroke="var(--card)" stroke-width="1.2">
              <ellipse cx="12" cy="12" rx="4.5" ry="10"/>
              <line x1="2" y1="12" x2="22" y2="12"/>
              <line x1="12" y1="2" x2="12" y2="22"/>
              <path d="M4 7 H20 M4 17 H20"/>
            </g>
          </svg>
          www.lindenwaeldchen.net
        </p>
        <p class="address">Marta Brecke, Grauer Pfad 7, 18471 Alt Feldow</p>
      </address>
    </article>
  </main>
</body>
</html>
```